Employee I.D. Card - Badge

We need an employee I.D. card designed. Our employees are going to be wearing these. I would like to have it look nice. Something professional yet cool (not uptight if that makes sense).
Project Scope:
Vertical orientation
Company name ------------- (Bright and Tidy)
Website ------------- (brightandtidymn.example)
Employee Picture
background check image
front and back designed - same design on either side
You can create the card without having the employee images on them.
Here are the dimensions -
2.125 x 3.370 inches
Double sided - same design can be used front and back
Background badge - I would like to add an image that shows that the employee has taken a background check. I've added the press-kit for the company we use. If you have a better idea than incorporating their logo, we can certainly do something different.
Example image-
https://www.lookupzone.example/find?q=background+check+badge&kind=images&ref=XyZ4qWm82LpRt:
The print company will set up the names.
Logo is attached
Also attached are our business cards. You can use this for an idea of brand/company style.
Our website - brightandtidymn.example

```html
<!DOCTYPE html>
<html lang="en">
<head>
<meta charset="utf-8">
<title>Bright and Tidy – Employee Badge</title>
<link href="https://fonts.googleapis.com/css2?family=Arimo:wght@400&display=swap" rel="stylesheet">
<style>
  :root {
    --page: #ffffff;
    --card-edge: #d9d9d9;
    --brand-blue: #1a86c8;
    --blue-dark: #1c6fb8;
    --lime-top: #c4d412;
    --lime-bottom: #9cc42a;
    --ring: #a9c63a;
    --muted: #8c8c8c;
    --photo: #d2d3d3;
    --seal-gold: #d9b24a;
    --seal-dark: #1f1f1f;
    --white: #ffffff;
  }
  * { box-sizing: border-box; margin: 0; padding: 0; }
  html, body {
    width: 1200px; height: 1200px; overflow: hidden;
    background: var(--page);
    font-family: "Arimo", Arial, sans-serif;
  }
  .badge-card {
    position: absolute;
    left: 325px; top: 164px;
    width: 550px; height: 870px;
    border: 1px solid var(--card-edge);
    background: var(--white);
    overflow: hidden;
  }
  .brand-name {
    position: absolute;
    left: 96px; top: 100px;
    width: 380px;
    color: var(--brand-blue);
    font-size: 78px;
    line-height: 0.98;
    font-weight: 400;
    letter-spacing: -2px;
  }
  .brand-dot {
    position: absolute;
    left: 128px; top: 92px;
    width: 18px; height: 18px;
    border-radius: 50%;
    background: var(--brand-blue);
  }
  .brand-site {
    position: absolute;
    right: 121px; top: 312px;
    color: var(--muted);
    font-size: 18px;
    letter-spacing: 0.2px;
  }
  .badge-art {
    position: absolute;
    left: 0; top: 0;
    width: 550px; height: 870px;
  }
  .employee {
    position: absolute;
    left: 339px; top: 610px;
    color: var(--white);
  }
  .employee-name {
    font-size: 42px;
    line-height: 44px;
    font-weight: 400;
    letter-spacing: 0.5px;
  }
  .employee-role {
    margin-top: 8px;
    font-size: 28px;
    line-height: 32px;
  }
</style>
</head>
<body>
  <div class="badge-card">
    <svg class="badge-art" viewBox="0 0 550 870" xmlns="http://www.w3.org/2000/svg">
      <defs>
        <linearGradient id="lime" x1="0" y1="0" x2="0" y2="1">
          <stop offset="0" stop-color="var(--lime-top)"/>
          <stop offset="1" stop-color="var(--lime-bottom)"/>
        </linearGradient>
        <linearGradient id="blueDot" x1="0" y1="0" x2="0" y2="1">
          <stop offset="0" stop-color="#2a9ee0"/>
          <stop offset="1" stop-color="var(--blue-dark)"/>
        </linearGradient>
        <linearGradient id="photoTone" x1="0" y1="0" x2="0" y2="1">
          <stop offset="0" stop-color="#dcdddd"/>
          <stop offset="1" stop-color="#c6c7c7"/>
        </linearGradient>
        <clipPath id="photoClip"><circle cx="199" cy="694" r="126"/></clipPath>
      </defs>

      <!-- name panel -->
      <circle class="name-panel" cx="475" cy="732" r="218" fill="url(#lime)"/>

      <!-- employee photo area -->
      <circle cx="199" cy="694" r="126" fill="var(--white)"/>
      <rect role="img" aria-label="Employee photo placeholder"
            x="73" y="568" width="252" height="252"
            clip-path="url(#photoClip)" fill="url(#photoTone)"/>
      <circle cx="199" cy="694" r="126" fill="none" stroke="var(--ring)" stroke-width="1.2"/>

      <!-- accent bubbles -->
      <circle cx="85" cy="562" r="17.5" fill="url(#lime)"/>
      <circle cx="124" cy="550" r="8" fill="url(#blueDot)"/>
      <circle cx="73" cy="794" r="17" fill="url(#blueDot)"/>
      <circle cx="487" cy="795" r="25" fill="var(--white)"/>

      <!-- background check seal -->
      <g class="check-seal" role="img" aria-label="Background check cleared seal">
        <circle cx="275" cy="792" r="46" fill="var(--seal-gold)"/>
        <circle cx="275" cy="792" r="38" fill="var(--seal-dark)"/>
        <circle cx="275" cy="792" r="18" fill="var(--seal-gold)"/>
        <path d="M266 792 l6 6 l12 -13" fill="none" stroke="var(--seal-dark)" stroke-width="4" stroke-linecap="round" stroke-linejoin="round"/>
      </g>
    </svg>

    <span class="brand-dot"></span>
    <h1 class="brand-name">Bright<br>and Tidy</h1>
    <p class="brand-site">brightandtidymn.example</p>

    <div class="employee">
      <p class="employee-name">SAM<br>LARK</p>
      <p class="employee-role">consultant</p>
    </div>
  </div>
</body>
</html>
```